Car rental website design for a UAE car rental company

This project is about creating a new website design for a car rental company located in Dubai (United Arab Emirates), I opened the same project a few months ago but I didn't receive a lot of appealing entries so I closed it but this time I am marking the project as guaranteed to avoid such situation again, if you have already provided a design before then please re-submit again on this project so that it is considered while reviewing all the designs

A few important things:

1- We need a simple non-complex design
2- The final deliverable would be 2 screens (PSD, JPEG ... etc), the first screen is for the home page and the second screen is for an internal page
3- The home page must have a section that end users can use to rent a car online directly from the home page instead of going into some inner pages
4- The current website is very old and not very appealing so avoid creating a similar design (www.quarvin-drive.example)
5- The name is Quarvin but the company rents normal cars (no Limousin cars will be rented) so avoid adding any fancy cars in the images/graphics used in the design, just normal end users cars
6- The expected pages would be: home, About us, Our team, Strategy, Contact us and links to social media pages
7- The attachments include the company's logo and some screens from other car rental companies that provide online rentals/payments

If you have any questions please feel free to ask and please note that we will need the designs urgently

Thanks

Target Market(s)

Dubai - United Arab Emirates

Industry/Entity Type

It Company

Number of Pages Required

2 page

Font styles to use
Sans Serif

Requirements
Must have
• Check the project details
Nice to have
Should not have

```html
<!DOCTYPE html>
<html lang="en">
<head>
<meta charset="utf-8">
<title>Quarvin Rent A Car</title>
<link href="https://fonts.googleapis.com/css2?family=Roboto+Slab:wght@300;400;700&family=Roboto+Condensed:wght@400&family=Open+Sans:wght@400;600&display=swap" rel="stylesheet">
<style>
:root{
  --crimson:#a3093e;
  --grey-text:#8a9490;
  --ink:#222;
  --body:#3a3a3a;
  --sage:#8f9c96;
  --band:#f3f3f3;
  --panel:#cfccd2;
  --field:#e4e2e6;
  --white:#fff;
  --placeholder-a:#eceeef;
  --placeholder-b:#d3d6d9;
}
*{box-sizing:border-box;margin:0;padding:0}
html,body{width:1121px;height:1200px;overflow:hidden;background:var(--white)}
body{position:relative;font-family:"Roboto Slab",serif;color:var(--body)}
.abs{position:absolute}

/* header */
.site-header{position:absolute;left:0;top:0;width:1121px;height:97px;background:linear-gradient(#f3f0f2,#e9e3e7);border-bottom:2px solid var(--crimson)}
.brand{left:75px;top:10px;display:flex;align-items:center;gap:10px}
.brand-square{width:72px;height:80px;border:3px solid var(--crimson);background:var(--white)}
.brand-name{font-family:"Roboto Slab",serif;font-weight:400;font-size:36px;color:var(--grey-text);line-height:1}
.brand-tag{font-family:"Roboto Slab",serif;font-weight:700;font-size:16px;letter-spacing:3px;color:var(--crimson);margin-top:4px;margin-left:30px}
.social{display:flex;gap:8px}
.social span{width:23px;height:23px;border-radius:50%;background:var(--sage);border:2px solid var(--white);box-shadow:0 0 0 1px #b7b7b7}
.social .s1{background:#3b5998}.social .s2{background:#3fa2d9}.social .s3{background:#1d7bb8}.social .s4{background:#d34836}
.header-social{left:563px;top:16px}
.call{left:788px;top:10px;display:flex;align-items:center;gap:8px;font-size:18px;color:var(--crimson)}
.main-nav{left:564px;top:66px;display:flex;gap:24px;font-size:16px;color:var(--grey-text);font-weight:300}
.main-nav .active{color:var(--crimson)}

/* hero */
.hero{left:0;top:99px;width:1121px;height:408px;background:linear-gradient(100deg,#3b2c45 0%,#7b4a4a 25%,#e88a3c 45%,#b45a4e 62%,#2d2441 100%)}
.hero-title{left:265px;top:125px;width:385px;text-align:center;font-family:"Roboto Condensed",sans-serif;font-weight:400;font-size:29px;line-height:35px;color:var(--white);white-space:nowrap}

/* booking */
.booking{left:655px;top:98px;width:391px;height:409px;background:var(--crimson);padding:4px}
.tabs{display:flex;height:38px;align-items:center}
.tab-active{background:var(--sage);color:var(--white);height:38px;line-height:42px;padding:0 10px;font-size:16px}
.tab{color:var(--white);font-size:15px;padding-left:8px;white-space:nowrap}
.booking-body{position:relative;background:var(--panel);height:363px;margin-top:1px;font-size:13.5px;color:#333}
.step{position:absolute;left:4px;width:24px;height:24px;border:1px solid var(--crimson);background:var(--white);text-align:center;line-height:22px;font-size:14px}
.bk{position:absolute;white-space:nowrap}
.link{color:var(--crimson);text-decoration:underline}
.field{position:absolute;height:26px;border:1px solid #8b8b8b;background:var(--field);font-size:12px;line-height:24px;padding-left:6px}
.spin{position:absolute;right:0;top:0;width:18px;height:24px;border-left:1px solid #8b8b8b;font-size:8px;line-height:11px;text-align:center}
.check{display:inline-block;width:9px;height:9px;border:1px solid #666;margin-right:5px;vertical-align:0}
.help{display:inline-block;width:20px;height:20px;border-radius:50%;background:var(--sage);color:var(--white);font-size:10px;text-align:center;line-height:20px;vertical-align:middle}
.quote-btn{position:absolute;right:8px;bottom:-8px;width:127px;height:44px;background:var(--crimson);color:var(--white);font-size:16px;text-align:center;line-height:40px}

/* features */
.features{left:0;top:509px;width:1121px;height:254px;background:var(--band);border-bottom:1px solid #e2e2e2}
.feature{position:absolute;top:31px;width:250px;text-align:center}
.feature-icon{width:88px;height:88px;border-radius:50%;border:2px solid #8a8f8d;background:var(--white);margin:0 auto;display:flex;align-items:center;justify-content:center}
.feature-icon.on{border-color:var(--crimson)}
.feature h3{font-weight:400;font-size:15px;line-height:20px;color:#333;margin-top:13px}
.feature p{font-family:"Open Sans",sans-serif;font-size:14px;line-height:19px;color:#444;margin:7px auto 0;width:200px}

/* content */
.section-title{font-size:18px;font-weight:300;color:var(--grey-text);padding-bottom:4px;border-bottom:1px dashed #aaa;width:437px}
.section-title em{font-style:normal;color:var(--crimson);font-weight:400}
.copy{font-size:13.5px;line-height:21px;color:#333}
.read-more{font-size:14.5px;color:var(--ink);margin-top:4px}
.divider{left:77px;top:960px;width:700px;height:8px;background:radial-gradient(ellipse at center,#d9d9d9 0%,rgba(255,255,255,0) 70%)}
.car-photo{position:absolute;width:200px;height:96px;background:linear-gradient(var(--placeholder-a),var(--placeholder-b))}
.price{position:absolute;height:38px;background:var(--crimson);color:var(--white);font-weight:700;font-size:16px;line-height:38px;text-align:center;white-space:nowrap}

/* footer */
.site-footer{left:0;top:1146px;width:1121px;height:54px;background:var(--crimson)}
.foot-nav{left:76px;top:18px;display:flex;gap:18px;font-size:14px;color:var(--white);font-weight:300}
.footer-social{left:623px;top:15px}
.copyright{left:814px;top:19px;font-family:"Open Sans",sans-serif;font-size:13.5px;color:var(--white)}
</style>
</head>
<body>

<header class="site-header">
  <div class="abs brand">
    <div class="brand-square"></div>
    <div>
      <div class="brand-name">Quarvin</div>
      <div class="brand-tag">Rent A Car</div>
    </div>
  </div>
  <div class="abs social header-social"><span class="s1"></span><span class="s2"></span><span class="s3"></span><span class="s4"></span></div>
  <div class="abs call">
    <svg width="36" height="42" viewBox="0 0 36 42" aria-hidden="true"><path d="M5 22 V16 A13 13 0 0 1 31 16 V22" fill="none" stroke="#666" stroke-width="3"/><rect x="2" y="19" width="7" height="12" rx="3" fill="var(--crimson)"/><rect x="27" y="19" width="7" height="12" rx="3" fill="var(--crimson)"/><path d="M30 31 Q30 38 20 38" fill="none" stroke="#666" stroke-width="2"/></svg>
    <span>Call us at +971 4 380 2716</span>
  </div>
  <nav class="abs main-nav"><span class="active">HOME</span><span>ABOUT US</span><span>OUR TEAM</span><span>STRATEGY</span><span>CONTACT US</span></nav>
</header>

<div class="abs hero" role="img" aria-label="Photo of a car driving along a road at sunset, lined with palm trees"></div>
<h1 class="abs hero-title">Experience An Extra Mile<br>of comfort, pleasure and<br>leisure From the best</h1>

<section class="abs booking">
  <div class="tabs"><div class="tab-active">Book A Car</div><div class="tab">View / Modify / Cancel A Reservation</div></div>
  <div class="booking-body">
    <div class="step" style="top:11px">1</div>
    <div class="bk" style="left:43px;top:12px">Pick-up Location &nbsp;(City, State or Airport Code</div>
    <div class="bk link" style="left:43px;top:34px">Previous Searches</div>
    <div class="field" style="left:43px;top:58px;width:325px">Dubai Airport - Terminal 3</div>
    <div class="bk link" style="left:43px;top:90px">Help me find a rental location</div>
    <div class="bk" style="left:43px;top:115px"><span class="check"></span>Return car to a different Rovena Location &nbsp;<span class="help">?</span></div>
    <div class="step" style="top:148px">2</div>
    <div class="bk" style="left:43px;top:149px">Pick-up Date &amp; Time</div>
    <div class="field" style="left:43px;top:173px;width:160px">26/03/2015</div>
    <div class="field" style="left:208px;top:173px;width:160px">16:00<span class="spin">^<br>v</span></div>
    <div class="bk" style="left:43px;top:210px">Return Date &amp; Time</div>
    <div class="field" style="left:43px;top:234px;width:160px">26/03/2015</div>
    <div class="field" style="left:208px;top:234px;width:160px">16:00<span class="spin">^<br>v</span></div>
    <div class="bk" style="left:43px;top:271px">Hire Car Type</div>
    <div class="field" style="left:43px;top:295px;width:160px">Automatic</div>
    <div class="bk" style="left:211px;top:296px;font-size:12.5px"><span class="check"></span>Apply a discount Code<span class="help">?</span></div>
    <div class="quote-btn">Get A Quote</div>
  </div>
</section>

<section class="abs features">
  <div class="feature" style="left:63px">
    <div class="feature-icon on"><svg width="60" height="44" viewBox="0 0 60 44" aria-hidden="true"><path d="M4 24 L9 12 H30 L35 24 V32 H4 Z" fill="var(--crimson)"/><path d="M24 32 L29 21 H50 L55 32 V40 H24 Z" fill="var(--crimson)" stroke="#fff" stroke-width="2"/><rect x="29" y="24" width="20" height="5" fill="#fff"/></svg></div>
    <h3>Wide Range Of Vehicles For City<br>Driving or SUV's For Trips</h3>
    <p>Lorem ipsum dolor sit aonsectetuer adipiscing elied diam nonummy</p>
  </div>
  <div class="feature" style="left:326px">
    <div class="feature-icon"><svg width="44" height="44" viewBox="0 0 44 44" aria-hidden="true"><path d="M8 22 L22 8 H34 V20 L20 34 Z" fill="#7d8582" transform="rotate(10 22 22)"/><circle cx="29" cy="14" r="2.5" fill="#fff"/><text x="15" y="27" font-size="9" fill="#fff" font-family="Open Sans">%</text></svg></div>
    <h3>Special 10% Discount For New<br>Customers On The First Rent</h3>
    <p>Lorem ipsum dolor sit aonsectetuer adipiscing elied diam nonummy</p>
  </div>
  <div class="feature" style="left:577px">
    <div class="feature-icon"><svg width="44" height="44" viewBox="0 0 44 44" aria-hidden="true"><circle cx="18" cy="8" r="4" fill="none" stroke="#7d8582" stroke-width="3"/><rect x="21" y="6" width="14" height="3" fill="#7d8582"/><path d="M6 30 L11 19 H33 L38 30 V38 H6 Z" fill="#7d8582"/><rect x="12" y="22" width="20" height="6" fill="#fff"/></svg></div>
    <h3>Long Term Car<br>Rentals</h3>
    <p>Lorem ipsum dolor sit aonsectetuer adipiscing elied diam nonummy</p>
  </div>
  <div class="feature" style="left:827px">
    <div class="feature-icon"><svg width="44" height="44" viewBox="0 0 44 44" aria-hidden="true"><path d="M18 8 L6 18 L18 28 V22 Q32 20 32 34 Q40 12 18 14 Z" fill="#7d8582"/></svg></div>
    <h3>Buyback Option After<br>Lease Term</h3>
    <p>Lorem ipsum dolor sit aonsectetuer adipiscing elied diam nonummy</p>
  </div>
</section>

<section class="abs" style="left:77px;top:792px;width:700px">
  <h2 class="section-title">Welcome to Quarvin <em>Rent A Car</em></h2>
  <p class="copy" style="margin-top:10px">As Dubai is expected to welcome millions of tourists and visitors, car rental industry is believed to escalate more rapidly in the region. Over the past five years, demands for car rentals in Dubai has been augmenting at a healthy pace and is currently registering a growth rate of 20 to 25 percent per year. The swift economic growth and the number. Quarvin was established to bring comfort and pleasure to all its clients. ...</p>
  <p class="read-more">Read More</p>
</section>
<div class="abs divider"></div>
<section class="abs" style="left:77px;top:999px;width:700px">
  <h2 class="section-title">Our <em>Mission</em></h2>
  <p class="copy" style="margin-top:14px">To be one of the leading auto leasing company in the fast growing economy and tourism industry of the emirate of Dubai &amp; play alongside with the major car rental companies in the globe.</p>
  <p class="copy" style="margin-top:4px;line-height:19px">Quarvin vows to deliver comfort, luxury &amp; satisfaction to all our clients by providing them professional, hassle-free and first class service.</p>
</section>

<div class="car-photo" style="left:834px;top:790px" role="img" aria-label="Photo of a silver sedan"></div>
<div class="price" style="left:834px;top:888px;width:199px">From Only AED 1100 p/m</div>
<div class="car-photo" style="left:837px;top:990px" role="img" aria-label="Photo of a red sedan"></div>
<div class="price" style="left:837px;top:1088px;width:193px">From Only AED 1100 p/m</div>

<footer class="abs site-footer">
  <nav class="abs foot-nav"><span>HOME</span><span>ABOUT US</span><span>OUR TEAM</span><span>STRATEGY</span><span>CONTACT US</span></nav>
  <div class="abs social footer-social"><span class="s1"></span><span class="s2"></span><span class="s3"></span><span class="s4"></span></div>
  <div class="abs copyright">© 2015 Quarvin. All Rights Reserved</div>
</footer>

</body>
</html>
```